business card double side design

We need a business card design for our company PLUMlearnhub. DOUBLE SIDED. We provide continuing education programs & courses across North America. Our website is www.plumlearnhub.example - please use the grey pinstrip concept as part of the design. Compliment the branding that is occuring on that site!
Please use pantones daa520 and 3f3151. Verdana for text. I have attached our logo.
I would like the logo & website address www.PLUMlearnhub.example on the front of the card, all other info on the backside. The final design should communicate authority and credibility.

• verdanda

• pantones daa520 and 3f3151. Verdana for text.
• must compliment the branding occuring on the www.PLUMlearnhub.example

```html
<!DOCTYPE html>
<html lang="en">
<head>
<meta charset="UTF-8">
<title>PLUMlearnhub Business Card – Front and Back</title>
<link href="https://fonts.googleapis.com/css2?family=Noto+Sans:wght@400;700;800&display=swap" rel="stylesheet">
<style>
  :root {
    --gold: #daa520;
    --gold-light: #e9b93a;
    --plum: #3f3151;
    --card-black: #050505;
    --strip-black: #121212;
    --white: #ffffff;
    --muted-white: #e6e6e6;
    --backdrop: #d6d6d4;
    --faint-mark: #0f0f0f;
  }
  * { margin: 0; padding: 0; box-sizing: border-box; }
  html, body {
    width: 1200px;
    height: 900px;
    overflow: hidden;
    background: var(--backdrop);
    font-family: Verdana, "Noto Sans", sans-serif;
  }
  .canvas {
    position: relative;
    width: 1200px;
    height: 900px;
  }
  .card {
    position: absolute;
    left: 300px;
    width: 600px;
    height: 343px;
    background: var(--card-black);
    overflow: hidden;
    box-shadow: 0 6px 18px rgba(0,0,0,0.25);
  }
  .card--front { top: 77px; }
  .card--back { top: 480px; }

  /* bottom band shared by both sides */
  .band-plum {
    position: absolute;
    left: 0; right: 0;
    bottom: 32px;
    height: 9px;
    background: var(--plum);
  }
  .band-gold {
    position: absolute;
    left: 0; right: 0;
    bottom: 0;
    height: 32px;
    background: linear-gradient(var(--gold) 0 40%, var(--gold-light) 40% 48%, var(--gold) 48% 100%);
  }

  /* front side */
  .front-mark {
    position: absolute;
    left: 40px;
    top: -20px;
    width: 230px;
    height: 230px;
    border-radius: 50%;
    background: var(--faint-mark);
  }
  .wordmark {
    position: absolute;
    font-weight: 700;
    color: var(--gold);
    letter-spacing: -0.5px;
    line-height: 1;
  }
  .card--front .wordmark {
    right: 38px;
    top: 178px;
    font-size: 44px;
  }
  .website {
    position: absolute;
    right: 38px;
    top: 240px;
    font-size: 17px;
    font-weight: 700;
    color: var(--gold);
  }

  /* back side */
  .seal {
    position: absolute;
    left: 40px;
    top: 78px;
    width: 86px;
    height: 86px;
    border-radius: 50%;
    background: var(--gold);
  }
  .card--back .wordmark {
    left: 142px;
    top: 104px;
    font-size: 38px;
  }
  .holder {
    position: absolute;
    right: 34px;
    top: 40px;
    text-align: right;
  }
  .holder__name {
    font-size: 20px;
    font-weight: 700;
    color: var(--gold);
    letter-spacing: 0.5px;
  }
  .holder__title {
    margin-top: 4px;
    font-size: 14px;
    color: var(--muted-white);
  }
  .contact-strip {
    position: absolute;
    left: 0; right: 0;
    bottom: 41px;
    height: 74px;
    background: var(--strip-black);
    display: flex;
    align-items: center;
    gap: 26px;
    padding: 0 30px;
  }
  .contact {
    display: flex;
    align-items: center;
    gap: 7px;
    font-size: 14.5px;
    color: var(--white);
    white-space: nowrap;
  }
  .contact svg { flex: none; }
</style>
</head>
<body>
<main class="canvas">

  <section class="card card--front" aria-label="Card front">
    <div class="front-mark" aria-hidden="true"></div>
    <div class="wordmark">PLUMlearnhub</div>
    <div class="website">www.PLUMlearnhub.example</div>
    <div class="band-plum"></div>
    <div class="band-gold"></div>
  </section>

  <section class="card card--back" aria-label="Card back">
    <div class="seal" aria-hidden="true"></div>
    <div class="wordmark">PLUMlearnhub</div>

    <div class="holder">
      <div class="holder__name">Dana Whitfield</div>
      <div class="holder__title">Founder/CEO</div>
    </div>

    <div class="contact-strip">
      <div class="contact">
        <svg width="11" height="15" viewBox="0 0 11 15" aria-hidden="true">
          <rect x="1" y="1" width="9" height="13" rx="1.5" fill="none" stroke="#daa520" stroke-width="1.6"/>
          <rect x="4" y="11" width="3" height="1.3" fill="#daa520"/>
        </svg>
        <span>555.014.2267</span>
      </div>
      <div class="contact">
        <svg width="13" height="13" viewBox="0 0 24 24" aria-hidden="true">
          <path fill="#daa520" d="M6.6 10.8a15.1 15.1 0 0 0 6.6 6.6l2.2-2.2c.3-.3.7-.4 1-.2 1.1.4 2.3.6 3.6.6.6 0 1 .4 1 1V20c0 .6-.4 1-1 1A17 17 0 0 1 3 4c0-.6.4-1 1-1h3.5c.6 0 1 .4 1 1 0 1.3.2 2.5.6 3.6.1.3 0 .7-.2 1z"/>
        </svg>
        <span>555.013.8840</span>
      </div>
      <div class="contact">
        <svg width="14" height="11" viewBox="0 0 14 11" aria-hidden="true">
          <rect x="0" y="0" width="14" height="11" fill="#daa520"/>
          <path d="M0 0 L7 6 L14 0" fill="none" stroke="#121212" stroke-width="1.3"/>
        </svg>
        <span>dana@PLUMlearnhub.example</span>
      </div>
    </div>

    <div class="band-plum"></div>
    <div class="band-gold"></div>
  </section>

</main>
</body>
</html>
```